Flyer for Car Detailing Shop

I am opening a detailing shop. I am looking for a nice, easy to read single sided flyer I can hand out at car shows, hang in store windows and to my clients and customers to promote my business. I want it a little professional yet attention grabbing. I want someone to look at it and go "holy shit, thats a nice flyer" haha

Here are some things that must be included:
- Company Name: Brightfern Motorworks Detailing & Coatings
- Tag Line: The Science of Detailing
- Address: 4150 Harlow Rd, Temperance, MI 48190
- www.brightfernmotor.example
- Find Us on social Media! ::insert facebook and plain orange circle
Colors: Black, Lime Green and Purple for accents, etc

HAND WASH
- Express Wash start at $25
- Deluxe Wash Start at $50

EXTERIOR DETAILING
-Basic Packages Start at $160
- Deluxe Packages Start at $350

INTERIOR DETAILING
- Basic Packages Start at $60
- Deluxe Packages Start at $200

New Car Prep and Ceramic Coatings
*Consultation required prior to beginning work*
- Paint: Starting at $500
- Interior: Starting at $100
- Wheels Off: Starting at $200
- Trim: Starting at $100
- Windows: $50 windshield/ $25 per pane

Additional Services
- Scratch removal
- Ozone Treatment
- Headlight Restoration
- Chip Repair

```html
<!DOCTYPE html>
<html lang="en">
<head>
<meta charset="utf-8">
<title>Brightfern Motorworks – The Science of Detailing</title>
<link rel="stylesheet" href="https://fonts.googleapis.com/css2?family=Poppins:wght@700;800&family=Raleway:wght@400;500;700;800&display=swap">
<style>
  :root{
    --green:#5fbf45;
    --green-dark:#3f8f2c;
    --purple:#4a1d83;
    --purple-deep:#2f0f5c;
    --charcoal:#2b2b2b;
    --ink:#1a1a1a;
    --paper:#f7f7f7;
    --line:#d9d9d9;
  }
  *{box-sizing:border-box;margin:0;padding:0}
  html,body{width:720px;height:1200px;overflow:hidden;background:var(--paper)}
  body{font-family:"Raleway",sans-serif;color:var(--ink)}
  .flyer{position:relative;width:720px;height:1200px;overflow:hidden;
    background:linear-gradient(180deg,#ffffff 0%,#f1f1f1 60%,#ebebeb 100%)}
  .layer{position:absolute;left:0;top:0;width:720px;height:1200px}

  .brand{position:absolute;left:30px;top:50px;width:250px;text-align:center}
  .brand-mark{width:70px;height:70px;border-radius:50%;background:var(--ink);margin:0 auto 18px}
  .brand-name{font-family:"Raleway",sans-serif;font-weight:800;font-size:25px;line-height:1.15;color:var(--ink)}

  .headline{position:absolute;left:30px;top:352px;font-family:"Poppins",sans-serif;font-weight:800;
    font-size:66px;line-height:1;letter-spacing:-1px}
  .headline .line-1{display:block;color:#fff}
  .headline .line-2{display:block;color:var(--green);margin:8px 0 0 84px}

  .section-title{font-family:"Raleway",sans-serif;font-weight:800;font-size:21px;color:var(--purple);
    line-height:1.05;padding-bottom:6px;border-bottom:3px solid var(--green);margin-bottom:12px}
  .col{position:absolute}
  .col-left{left:32px;width:298px;top:570px}
  .col-right{left:392px;width:298px;top:612px}
  .divider{position:absolute;left:358px;top:600px;width:2px;height:460px;background:var(--line)}

  .price-list{list-style:none}
  .price-list li{display:flex;align-items:center;font-size:16.5px;height:30px}
  .price-list .tick{width:15px;height:15px;margin-right:12px;flex:none}
  .price-list .label{flex:1}
  .price-list .label em{font-style:normal;color:var(--green-dark)}
  .price-list .price{width:42px;text-align:left}
  .note{font-weight:700;font-size:16.5px;line-height:1.25;margin:16px 0 8px}
  .block + .block{margin-top:34px}

  .pill{display:inline-block;background:var(--green);color:var(--ink);font-weight:800;font-size:21px;
    padding:5px 14px 6px;border-radius:0 16px 16px 0;margin:20px 0 10px}
  .extra-list{list-style:none}
  .extra-list li{display:flex;align-items:center;font-size:21px;height:34px;font-weight:500}
  .extra-list .dot{width:26px;height:26px;border-radius:50%;background:var(--green);margin-right:16px;flex:none;
    display:flex;align-items:center;justify-content:center}
  .extra-list .dot span{width:10px;height:10px;background:var(--charcoal);border-radius:2px}

  .contact{position:absolute;left:30px;top:1098px;list-style:none;color:#fff}
  .contact li{display:flex;align-items:center;font-size:22px;font-weight:500;height:32px}
  .contact svg{width:22px;height:22px;margin-right:22px;flex:none}

  .social-tag{position:absolute;left:480px;top:1072px;background:var(--green);color:var(--ink);
    font-weight:800;font-size:16px;padding:5px 14px;border-radius:14px 0 0 0}
  .social-icons{position:absolute;left:580px;top:1130px;display:flex;gap:14px}
  .social-icons span{width:46px;height:46px;border-radius:50%}
  .social-a{background:#3b5aa8}
  .social-b{background:#e8662d}
</style>
</head>
<body>
<div class="flyer">

  <svg class="layer" role="img" aria-label="Photo of a detailer in safety glasses polishing a dark car beside its wheel in a dim garage" viewBox="0 0 720 1200">
    <defs>
      <linearGradient id="photoTone" x1="0" y1="0" x2="1" y2="1">
        <stop offset="0" stop-color="#6b3a32"/>
        <stop offset="0.35" stop-color="#3a2a2a"/>
        <stop offset="0.7" stop-color="#1d1d20"/>
        <stop offset="1" stop-color="#3c3c40"/>
      </linearGradient>
    </defs>
    <polygon points="355,0 720,0 720,612 235,222" fill="url(#photoTone)"/>
  </svg>

  <svg class="layer" viewBox="0 0 720 1200" aria-hidden="true">
    <defs>
      <linearGradient id="bandTone" x1="0" y1="0" x2="1" y2="0">
        <stop offset="0" stop-color="#333"/>
        <stop offset="0.7" stop-color="#3a3a3a" stop-opacity="0.95"/>
        <stop offset="1" stop-color="#444" stop-opacity="0.2"/>
      </linearGradient>
    </defs>
    <polygon points="318,0 358,0 248,218 230,226" fill="var(--green)"/>
    <polygon points="0,360 330,200 720,570 720,612 0,520" fill="url(#bandTone)"/>
    <polygon points="0,520 720,612 720,622 0,532" fill="var(--green)"/>
    <!-- footer -->
    <rect x="420" y="1100" width="300" height="100" fill="var(--charcoal)"/>
    <polygon points="0,1090 465,1080 590,1200 0,1200" fill="var(--purple)"/>
    <polygon points="300,1084 465,1080 590,1200 520,1200" fill="var(--purple-deep)" opacity="0.6"/>
    <polygon points="465,1080 475,1080 600,1200 590,1200" fill="var(--green)"/>
  </svg>

  <div class="brand">
    <div class="brand-mark"></div>
    <p class="brand-name">Brightfern Motorworks Detailing &amp; Coatings</p>
  </div>

  <h1 class="headline"><span class="line-1">The Science</span><span class="line-2">of Detailing</span></h1>

  <svg width="0" height="0" style="position:absolute" aria-hidden="true">
    <symbol id="tick" viewBox="0 0 16 16">
      <circle cx="8" cy="8" r="6.5" fill="none" stroke="#4a1d83" stroke-width="1.5"/>
      <path d="M4.8 8.2l2.2 2.2 4.6-4.8" fill="none" stroke="#4a1d83" stroke-width="1.6"/>
    </symbol>
  </svg>

  <div class="divider"></div>

  <section class="col col-left">
    <div class="block">
      <h2 class="section-title">HAND WASH</h2>
      <ul class="price-list">
        <li><svg class="tick"><use href="#tick"/></svg><span class="label">Express Wash start at</span><span class="price">$25</span></li>
        <li><svg class="tick"><use href="#tick"/></svg><span class="label">Deluxe Wash Start at</span><span class="price">$50</span></li>
      </ul>
    </div>
    <div class="block">
      <h2 class="section-title">NEW CAR PREP<br>AND CERAMIC COATINGS</h2>
      <p class="note">Consultation required prior to beginning work</p>
      <ul class="price-list">
        <li><svg class="tick"><use href="#tick"/></svg><span class="label"><em>Paint:</em> Starting at</span><span class="price">$500</span></li>
        <li><svg class="tick"><use href="#tick"/></svg><span class="label"><em>Interior:</em> Starting at</span><span class="price">$100</span></li>
        <li><svg class="tick"><use href="#tick"/></svg><span class="label"><em>Wheels Off:</em> Starting at</span><span class="price">$200</span></li>
        <li><svg class="tick"><use href="#tick"/></svg><span class="label"><em>Trim:</em> Starting at</span><span class="price">$100</span></li>
        <li><svg class="tick"><use href="#tick"/></svg><span class="label"><em>Windows</em> at</span><span class="price">$50</span></li>
        <li><svg class="tick"><use href="#tick"/></svg><span class="label"><em>windshield</em> per pane at</span><span class="price">$25</span></li>
      </ul>
    </div>
  </section>

  <section class="col col-right">
    <div class="block">
      <h2 class="section-title">EXTERIOR DETAILING</h2>
      <ul class="price-list">
        <li><svg class="tick"><use href="#tick"/></svg><span class="label">Basic Packages Start at</span><span class="price">$160</span></li>
        <li><svg class="tick"><use href="#tick"/></svg><span class="label">Deluxe Packages Start at</span><span class="price">$350</span></li>
      </ul>
    </div>
    <div class="block">
      <h2 class="section-title">INTERIOR DETAILING</h2>
      <ul class="price-list">
        <li><svg class="tick"><use href="#tick"/></svg><span class="label">Basic Packages Start at</span><span class="price">$60</span></li>
        <li><svg class="tick"><use href="#tick"/></svg><span class="label">Deluxe Packages Start at</span><span class="price">$200</span></li>
      </ul>
    </div>
    <div class="pill">ADDITIONAL SERVICES</div>
    <ul class="extra-list">
      <li><span class="dot"><span></span></span>Scratch removal</li>
      <li><span class="dot"><span></span></span>Ozone Treatment</li>
      <li><span class="dot"><span></span></span>Headlight Restoration</li>
      <li><span class="dot"><span></span></span>Chip Repair</li>
    </ul>
  </section>

  <ul class="contact">
    <li>
      <svg viewBox="0 0 22 22" aria-hidden="true"><circle cx="11" cy="11" r="11" fill="#5fbf45"/><rect x="5.5" y="7" width="11" height="8" fill="#2b2b2b"/><path d="M5.5 7l5.5 4.5L16.5 7" fill="none" stroke="#5fbf45" stroke-width="1.2"/></svg>
      Jordan@brightfernmotor.example
    </li>
    <li>
      <svg viewBox="0 0 22 22" aria-hidden="true"><circle cx="11" cy="11" r="11" fill="#5fbf45"/><circle cx="11" cy="11" r="6" fill="none" stroke="#2b2b2b" stroke-width="1.4"/><path d="M5 11h12M11 5c-3 3.5-3 8.5 0 12M11 5c3 3.5 3 8.5 0 12" fill="none" stroke="#2b2b2b" stroke-width="1.2"/></svg>
      www.brightfernmotor.example
    </li>
    <li>
      <svg viewBox="0 0 22 22" aria-hidden="true"><circle cx="11" cy="11" r="11" fill="#5fbf45"/><path d="M11 17.5c-3-4-4.5-6-4.5-8a4.5 4.5 0 0 1 9 0c0 2-1.5 4-4.5 8z" fill="#2b2b2b"/><circle cx="11" cy="9.5" r="1.6" fill="#5fbf45"/></svg>
      4150 Harlow Rd, Temperance, MI 48190
    </li>
  </ul>

  <div class="social-tag">Find Us on social Media!</div>
  <div class="social-icons">
    <span class="social-a"></span>
    <span class="social-b"></span>
  </div>

</div>
</body>
</html>
```